Skincare company needing leaflet/flyer for selling products

Hi guys. I am needing a leaflet/flyer design for my new skincare business - Tovani skincare. Our products are all made in Australia from natural ingredients. The leaflet should specify that all products have - organic ingredients, cruelty free, no nasty chemicals or ingredients and a made in Australia logo.
The pictures I have supplied, if they can be made more professional looking for the design without any background that would be great. It should look like other competitors and very appealing. The leaflet can be double sided so it looks more easy to read
The information is provided as follows:
Product, skin types the product is for, ml capacity of bottle, key ingredients and price.
Contact is a whatsapp number and website will be up later so if a leaflet can be made with and without the website.
This leaflet/flyer can be easy to read, not hard on the eyes and easy to understand. Focus on blue shades and other calm colours to make it easy on the eyes and attractive to see. Thank you guys for helping
Getting professional product photos done that can be updated on the leaflet/flyers once received. More submissions are welcomed
People wanting good quality skincare that does not contain harmful chemicals and is organic

```html
<!DOCTYPE html>
<html lang="en">
<head>
<meta charset="utf-8">
<title>Tovani Skincare – Product Flyer</title>
<link href="https://fonts.googleapis.com/css2?family=Poppins:wght@400;500;600;700&display=swap" rel="stylesheet">
<style>
  :root {
    --stage: #eceff0;
    --teal: #4fcfbd;
    --teal-soft: #a9e9df;
    --mint: #d9f5f0;
    --mint-deep: #bdeee5;
    --forest: #1d6a58;
    --forest-dark: #0f5646;
    --ink: #2f3b39;
    --grey: #e6e8ea;
    --white: #ffffff;
  }
  * { box-sizing: border-box; margin: 0; padding: 0; }
  html, body { width: 1200px; height: 675px; overflow: hidden; }
  body {
    background: var(--stage);
    font-family: "Poppins", sans-serif;
    color: var(--ink);
    position: relative;
  }
  .page {
    position: absolute;
    top: 38px;
    width: 424px;
    height: 600px;
    overflow: hidden;
    box-shadow: 0 6px 24px rgba(0,0,0,.12);
  }

  /* ---------- Front ---------- */
  .front {
    left: 150px;
    background: linear-gradient(170deg, #f4f5f6 0%, #e9ebec 60%, #dfe2e3 100%);
  }
  .front-wave {
    position: absolute; left: 0; top: 0; width: 424px; height: 260px;
  }
  .portrait {
    position: absolute; right: 0; top: 0; width: 250px; height: 500px;
    background: radial-gradient(ellipse at 45% 30%, #f1dccd 0%, #e8d2c3 30%, #f2f0ee 70%, rgba(242,240,238,0) 100%);
  }
  .product-shot {
    position: absolute; left: 40px; top: 250px; width: 290px; height: 320px;
    border-radius: 18px;
    background: radial-gradient(ellipse at 50% 55%, #ffffff 0%, #f3f3f1 45%, rgba(226,229,230,0) 80%);
  }
  .brand {
    position: absolute; left: 30px; top: 88px;
    color: var(--white); font-weight: 700; line-height: 1;
  }
  .brand-name { font-size: 44px; letter-spacing: .5px; }
  .brand-sub { font-size: 15px; letter-spacing: 3px; text-transform: uppercase; margin-top: 6px; padding-left: 60px; }
  .badge {
    position: absolute; width: 70px; height: 70px; border-radius: 50%;
    background: var(--teal);
    border: 3px solid rgba(255,255,255,.85);
    box-shadow: 0 0 0 3px var(--teal-soft);
    display: flex; flex-direction: column; align-items: center; justify-content: center;
    color: var(--white); text-align: center;
  }
  .badge svg { width: 22px; height: 22px; margin-bottom: 3px; }
  .badge-label { font-size: 6.5px; font-weight: 600; line-height: 1.2; }
  .badge-natural { left: 318px; top: 355px; }
  .badge-chemicals { left: 336px; top: 445px; }
  .origin {
    position: absolute; left: 318px; top: 532px;
    font-size: 17px; font-weight: 700; line-height: 1.15; color: #3a3f3e;
  }

  /* ---------- Back ---------- */
  .back {
    left: 626px;
    background: linear-gradient(160deg, #eaf8f5 0%, var(--mint) 45%, #b7efe5 100%);
  }
  .section-title { font-size: 14px; font-weight: 700; color: var(--forest); }
  .intro { position: absolute; left: 24px; top: 24px; width: 376px; }
  .intro p { font-size: 6.5px; line-height: 1.5; color: #3f5550; margin-top: 4px; }
  .product {
    position: absolute; display: flex; align-items: center; gap: 8px;
  }
  .product-photo {
    width: 64px; height: 64px; border-radius: 50%;
    background: radial-gradient(circle at 50% 50%, #ffffff 0%, #f1f3f3 60%, #e2e6e6 100%);
    border: 3px solid var(--white);
    box-shadow: 0 0 0 2px var(--teal-soft);
  }
  .product-info { color: var(--forest); line-height: 1.1; }
  .product-type { font-size: 6.5px; font-weight: 600; }
  .product-price { font-size: 18px; font-weight: 600; }
  .product-cap { font-size: 6.5px; font-weight: 700; }
  .product-ml { font-size: 6px; color: var(--teal); font-weight: 600; }
  .p1 { left: 22px; top: 118px; }
  .p2 { left: 150px; top: 88px; }
  .p3 { left: 285px; top: 66px; }
  .p4 { left: 62px; top: 206px; }
  .p5 { left: 200px; top: 182px; }

  .skin-panel {
    position: absolute; left: 0; top: 292px; width: 424px; height: 320px;
    background: linear-gradient(180deg, #c4f0e8 0%, #d6f6f0 100%);
    border-radius: 34px 34px 0 0;
  }
  .skin-panel .section-title { position: absolute; left: 24px; top: 18px; font-size: 12px; }
  .skin-types {
    position: absolute; left: 22px; top: 46px; width: 380px;
    display: flex; justify-content: space-between; list-style: none;
  }
  .skin-type { width: 62px; text-align: center; font-size: 6.5px; font-weight: 600; color: var(--forest); }
  .skin-avatar {
    width: 62px; height: 62px; border-radius: 50%; margin-bottom: 5px;
    background: linear-gradient(180deg, #5fcbbb 0%, #5fcbbb 35%, #f7d3b4 36%, #f3c8a6 100%);
    border: 3px solid var(--white);
  }

  .info-panel {
    position: absolute; left: 0; top: 455px; width: 424px; height: 150px;
    background: var(--white);
    border-radius: 36px 0 0 0;
  }
  .ingredients { position: absolute; left: 24px; top: 20px; width: 200px; }
  .ingredients p { font-size: 6.5px; line-height: 1.55; color: #3f5550; margin-top: 5px; }
  .note { position: absolute; font-size: 6.5px; line-height: 1.4; color: var(--forest); text-align: right; }
  .note strong { display: block; font-weight: 700; font-size: 7px; }
  .note-order { left: 244px; top: 22px; width: 80px; }
  .note-cruelty { left: 330px; top: 22px; width: 78px; }
  .contact-bar {
    position: absolute; left: 232px; top: 84px; width: 192px; height: 22px;
    background: var(--forest-dark);
    display: flex; align-items: center; justify-content: flex-end; gap: 5px;
    padding-right: 14px; color: var(--white); font-size: 7px; font-weight: 500;
    border-radius: 11px 0 0 11px;
  }
  .contact-bar svg, .web-pill svg { width: 9px; height: 9px; }
  .web-pill {
    position: absolute; left: 232px; top: 114px; height: 18px; padding: 0 10px;
    background: var(--forest); color: var(--white); border-radius: 9px;
    display: flex; align-items: center; gap: 5px; font-size: 6.5px;
  }
</style>
</head>
<body>

<!-- Front side -->
<section class="page front">
  <svg class="front-wave" viewBox="0 0 424 260" preserveAspectRatio="none" aria-hidden="true">
    <defs>
      <linearGradient id="waveFill" x1="0" y1="0" x2="1" y2="1">
        <stop offset="0" stop-color="#3fc7b3"/>
        <stop offset=".6" stop-color="#7fd9cb"/>
        <stop offset="1" stop-color="#e9ebec" stop-opacity="0"/>
      </linearGradient>
    </defs>
    <path d="M0 0 H200 C160 40 170 100 120 150 C80 190 30 220 0 240 Z" fill="url(#waveFill)"/>
  </svg>
  <div class="portrait" role="img" aria-label="Photo of a smiling woman applying cream to her cheek"></div>
  <div class="product-shot" role="img" aria-label="Product photo: pump bottle, serum dropper, eye cream tube and body balm jar"></div>

  <div class="brand">
    <div class="brand-name">Tovani</div>
    <div class="brand-sub">Skincare</div>
  </div>

  <div class="badge badge-natural">
    <svg viewBox="0 0 24 24" fill="#fff" aria-hidden="true"><path d="M20 3C9 3 4 9 4 16c0 2 .5 3.5 1 5l1.5-1c-.3-1-.5-2-.5-3 5-1 9-4 11-9-2 4-6 7-10 8 0-6 4-11 13-13z"/></svg>
    <span class="badge-label">100% Natural<br>Ingredients</span>
  </div>
  <div class="badge badge-chemicals">
    <svg viewBox="0 0 24 24" fill="none" stroke="#fff" stroke-width="2" aria-hidden="true"><path d="M9 3h6M10 3v6L5 19a2 2 0 0 0 2 3h10a2 2 0 0 0 2-3l-5-10V3"/><path d="M4 4l16 16"/></svg>
    <span class="badge-label">No Dangerous<br>Chemicals</span>
  </div>

  <p class="origin">Made in<br>Australia</p>
</section>

<!-- Back side -->
<section class="page back">
  <div class="intro">
    <h2 class="section-title">Product Types</h2>
    <p>Every formula is blended in small batches from plant oils, botanical extracts and gentle actives, chosen to calm, hydrate and protect the skin without harsh additives or synthetic fragrance.</p>
  </div>

  <div class="product p1">
    <div class="product-photo" role="img" aria-label="Pump bottle cleanser"></div>
    <div class="product-info"><div class="product-type">Product Type</div><div class="product-price">$12</div><div class="product-cap">Capacity</div><div class="product-ml">30 mL</div></div>
  </div>
  <div class="product p2">
    <div class="product-photo" role="img" aria-label="Tall lotion bottle"></div>
    <div class="product-info"><div class="product-type">Product Type</div><div class="product-price">$12</div><div class="product-cap">Capacity</div><div class="product-ml">500 mL</div></div>
  </div>
  <div class="product p3">
    <div class="product-photo" role="img" aria-label="Body balm jar"></div>
    <div class="product-info"><div class="product-type">Product Type</div><div class="product-price">$12</div><div class="product-cap">Capacity</div><div class="product-ml">100 mL</div></div>
  </div>
  <div class="product p4">
    <div class="product-photo" role="img" aria-label="Eye cream pump tube"></div>
    <div class="product-info"><div class="product-type">Product Type</div><div class="product-price">$12</div><div class="product-cap">Capacity</div><div class="product-ml">30 mL</div></div>
  </div>
  <div class="product p5">
    <div class="product-photo" role="img" aria-label="Serum dropper bottle"></div>
    <div class="product-info"><div class="product-type">Product Type</div><div class="product-price">$12</div><div class="product-cap">Capacity</div><div class="product-ml">30 mL</div></div>
  </div>

  <div class="skin-panel">
    <h2 class="section-title">Skin Type The Product is For</h2>
    <ul class="skin-types">
      <li class="skin-type"><div class="skin-avatar" role="img" aria-label="Illustration for normal skin"></div>Normal</li>
      <li class="skin-type"><div class="skin-avatar" role="img" aria-label="Illustration for dry skin"></div>Dry</li>
      <li class="skin-type"><div class="skin-avatar" role="img" aria-label="Illustration for oily skin"></div>Oily</li>
      <li class="skin-type"><div class="skin-avatar" role="img" aria-label="Illustration for sensitive skin"></div>Sensitive</li>
      <li class="skin-type"><div class="skin-avatar" role="img" aria-label="Illustration for acne-prone skin"></div>Acne</li>
    </ul>
  </div>

  <div class="info-panel">
    <div class="ingredients">
      <h2 class="section-title">Key Ingredients</h2>
      <p>Aloe vera, jojoba oil, kakadu plum, rosehip and vitamin E work together to nourish and soothe, restoring balance and a healthy glow. All ingredients are sourced from trusted Australian growers.</p>
    </div>
    <div class="note note-order"><strong>Order Now</strong>Message us any day for fast replies</div>
    <div class="note note-cruelty"><strong>Cruelty Free</strong>Never tested on animals</div>
    <div class="contact-bar">
      <svg viewBox="0 0 24 24" fill="#fff" aria-hidden="true"><path d="M6.6 10.8a15 15 0 0 0 6.6 6.6l2.2-2.2a1 1 0 0 1 1-.25 11.4 11.4 0 0 0 3.6.57 1 1 0 0 1 1 1V20a1 1 0 0 1-1 1A17 17 0 0 1 3 4a1 1 0 0 1 1-1h3.5a1 1 0 0 1 1 1c0 1.25.2 2.45.57 3.6a1 1 0 0 1-.25 1z"/></svg>
      123-456-7890
    </div>
    <div class="web-pill">
      <svg viewBox="0 0 24 24" fill="none" stroke="#fff" stroke-width="2" aria-hidden="true"><circle cx="12" cy="12" r="9"/><path d="M3 12h18M12 3a14 14 0 0 1 0 18M12 3a14 14 0 0 0 0 18"/></svg>
      website.website.com
    </div>
  </div>
</section>

</body>
</html>
```